Web Design Project

We are an IT System Integrator. We provide Norvik 500 ERP System, CRM etc. We also provide hardware, networking servicing. Please look at www.brinquot.com.sg. They provide the same service as us. We like to redesign our web site. I will attached the color that I prefer for reference.

Our website is www.ravdu.com.sg.  It has been created about 14 years ago.  We are trying to revamp it with a new look and information.   The new website must be informative, fast.    I have attached an attachment which show the color that I prefer(brownish golden).   

Our competitor (www.brinquot.com) is carrying the same trade as us.  They have all the informations In their website that we will like to have.  Therefore I recommend you to take a look at my competitor website and have a better   
understanding on the kind of information I would like to have for my new website.

This project is guarantee to the person with the best design.  We can have it guarantee.

Target Market(s)

Corporate and companies

Industry/Entity Type

Hardware

```html
<!DOCTYPE html>
<html lang="en">
<head>
<meta charset="utf-8">
<title>Ravdu Information Systems PTE LTD</title>
<link href="https://fonts.googleapis.com/css2?family=Oswald:wght@400;500&family=Arimo:wght@400;700&display=swap" rel="stylesheet">
<style>
:root{
  --gold:#c8960f;
  --gold-dark:#8a5e08;
  --brown:#7a5310;
  --text:#333;
  --muted:#666;
  --panel:#e4e4e4;
  --panel-edge:#c9c9c9;
  --page:#ffffff;
  --nav:#555;
}
*{box-sizing:border-box;margin:0;padding:0}
html,body{width:879px;height:1200px;overflow:hidden;background:var(--page)}
body{position:relative;font-family:Arimo,Arial,sans-serif;color:var(--text);font-size:10px}
.abs{position:absolute}
.header{left:0;top:0;width:879px;height:100px;background:linear-gradient(#fff,#e9e9e9)}
.util-tab{left:607px;top:0;width:183px;height:24px;background:linear-gradient(#b8860b,#7d5507);border-radius:0 0 8px 8px;color:#fff;font:500 11px Oswald,sans-serif;display:flex;justify-content:center;align-items:center;gap:8px}
.brand{left:118px;top:26px;display:flex;align-items:center;gap:8px;color:var(--gold-dark);font:500 30px Oswald,sans-serif;letter-spacing:1px}
.brand i{width:34px;height:34px;border-radius:50%;background:var(--gold);display:block}
.contact{left:612px;top:34px;font-size:10px;color:#444;line-height:17px}
.contact svg{vertical-align:-2px;margin-right:5px}
.nav{left:389px;top:72px;display:flex;font:400 12px Oswald,sans-serif;color:var(--nav)}
.nav span{padding:6px 11px;height:28px}
.nav .active{background:#fff;color:var(--gold);border:1px solid #ddd;border-bottom:none;border-radius:3px 3px 0 0}
.band{left:0;top:100px;width:879px;height:316px;background:linear-gradient(#c99a16,#b07f08 70%,#a06f04)}
.site-title{left:0;top:108px;width:879px;text-align:center;font:500 44px Oswald,sans-serif;letter-spacing:1px;color:#eee;background:linear-gradient(#fff,#aeb3b8);-webkit-background-clip:text;background-clip:text;-webkit-text-fill-color:transparent}
.slider{left:88px;top:172px;width:703px;height:292px;border-radius:4px;background:linear-gradient(100deg,#e6f0f8,#b7d1e6 45%,#2c4f7a 75%,#1c2e48);box-shadow:0 12px 20px rgba(0,0,0,.25)}
.caption{left:88px;top:270px;width:320px;height:105px;background:rgba(40,40,40,.85);padding:6px 0 0 63px}
.caption h2{font:500 28px Oswald,sans-serif;color:#e0a321}
.caption p{color:#fff;font-size:13px;line-height:15px}
.arrow{width:32px;height:32px;border-radius:50%;background:#fff;box-shadow:0 1px 3px rgba(0,0,0,.4)}
h1.welcome{left:89px;top:520px;font:500 20px Oswald,sans-serif;color:var(--brown)}
.para{font-size:9.5px;line-height:12.6px;color:#444}
.divider{left:573px;top:514px;width:1px;height:523px;background:#e2e2e2}
.photo{left:416px;top:633px;width:130px;height:102px;background:linear-gradient(#f1f4f7,#c5ccd4 60%,#3a4250)}
.news{left:89px;top:790px;width:457px;height:242px;background:linear-gradient(#f2f2f2,#d3d3d3);border-radius:4px;box-shadow:0 2px 3px rgba(0,0,0,.2)}
.news-head{height:30px;background:linear-gradient(#a9790c,#7d5507);border-radius:4px 4px 0 0;color:#fff;font:500 14px Oswald,sans-serif;padding:5px 20px;display:flex;justify-content:space-between}
.news-head b{font-weight:500;letter-spacing:4px;font-size:12px}
.news-head b em{color:#f5c542;font-style:normal}
.item{padding:12px 20px 0 22px;position:relative}
.item h3{font-size:11px;font-weight:400;color:#222;margin-left:45px}
.item .date{font-style:italic;font-size:9px;color:#555;margin-left:45px}
.item p{font-size:8.8px;line-height:11.5px;color:#444;margin-top:12px}
.item + .item{border-top:1px solid #e8e8e8;margin-top:12px}
.cal-ico{position:absolute;left:22px;top:12px}
.box{left:597px;width:195px;background:linear-gradient(#f4f4f4,#d2d2d2);border:1px solid var(--panel-edge);border-radius:3px;box-shadow:0 2px 3px rgba(0,0,0,.15)}
.box h4{text-align:center;font:400 15px Oswald,sans-serif;color:#555;padding:6px 0;background:linear-gradient(#f4f4f4,#e6e6e6)}
.field{display:flex;align-items:center;margin:8px 12px 0 13px;font-size:11px;color:#333}
.field span{width:58px}
.field i{flex:1;height:19px;background:#fff;border:1px solid #ccc}
.submit{float:right;margin:10px 12px 0;background:linear-gradient(#b98a1f,#7d5507);color:#fff;font:500 13px Oswald,sans-serif;padding:2px 8px;border-radius:2px}
.quote{margin:14px 16px 0 17px;font-size:11px;color:#222}
.quote em{display:block;font-size:9px;color:#555}
.quote p{font-size:9px;line-height:11px;color:#666;margin:6px 10px 0 20px}
.calendar{margin:4px 12px 0 12px;width:170px}
.cal-head{height:22px;background:linear-gradient(#9c6e08,#7a5206);color:#fff;font:500 12px Oswald,sans-serif;display:flex;justify-content:space-between;align-items:center;padding:0 8px}
.cal-head small{font-size:9px}
table.cal{width:170px;table-layout:fixed;border-collapse:collapse;font-size:9.5px;text-align:center}
.cal th{font-size:6.5px;font-weight:700;background:#f2f2f2;color:#333;height:12px;padding:0}
.cal td{border:1px solid #fff;background:#e2e2e2;height:18px;color:#444}
.cal .o{color:#aaa;background:#ececec}
.cal .h{color:var(--gold-dark);font-weight:700}
.partners{left:0;top:1076px;width:879px;height:70px;background:linear-gradient(#e6e6e6,#f8f8f8);display:flex;justify-content:center;align-items:center;gap:62px;color:#9a9a9a;font:500 22px Oswald,sans-serif}
.partners i{width:34px;height:34px;border-radius:50%;background:#c4c4c4;display:block}
.partners .small{font-size:17px}
.footer-links{left:89px;top:1172px;font-size:8.5px;color:#444;word-spacing:3px}
.social{left:390px;top:1161px;display:flex;gap:4px}
.social i{width:33px;height:33px;border-radius:50%;background:#c8c8c8;display:block}
.copy{right:88px;top:1172px;font-size:8.5px;color:#444}
</style>
</head>
<body>
<header class="header abs"></header>
<div class="util-tab abs"><span>FAQs</span>•<span>Resources</span>•<span>Contact Us</span></div>
<div class="brand abs"><i></i>RIS</div>
<div class="contact abs">
  <div><svg width="10" height="10" viewBox="0 0 10 10"><path d="M2 0l2 2-1 2 3 3 2-1 2 2-2 2C3 10 0 7 0 2z" fill="#b03a1a"/></svg>(65) 6380 2194</div>
  <div><svg width="11" height="8" viewBox="0 0 11 8"><rect width="11" height="8" fill="#c98b3a"/><path d="M0 0l5.5 4.5L11 0" stroke="#fff" fill="none"/></svg>sales@ravduinfosystems.com</div>
</div>
<nav class="nav abs"><span class="active">Home</span><span>About Us</span><span>Services</span><span>Solutions</span><span>Event and Promotion</span><span>Our Clients</span></nav>

<div class="band abs"></div>
<div class="site-title abs">RAVDU INFORMATION SYSTEMS PTE LTD</div>
<div class="slider abs" role="img" aria-label="Photo of a smiling business team giving thumbs up at a laptop"></div>
<div class="caption abs"><h2>NULLA LOBORTIS</h2><p>Lorem ipsum dolor sit amet, consectetur adipiscing elit. Nulla lobortis consequat mauris, eget eleifend nunc viverra</p></div>
<svg class="arrow abs" style="left:100px;top:305px" viewBox="0 0 32 32"><circle cx="16" cy="16" r="16" fill="#fff"/><path d="M18 10l-6 6 6 6" stroke="#555" stroke-width="2" fill="none"/></svg>
<svg class="arrow abs" style="left:749px;top:305px" viewBox="0 0 32 32"><circle cx="16" cy="16" r="16" fill="#fff"/><path d="M14 10l6 6-6 6" stroke="#555" stroke-width="2" fill="none"/></svg>

<h1 class="welcome abs">Welcome to Ravdu Information Systems PTE LTD</h1>
<p class="para abs" style="left:89px;top:566px;width:457px">Lorem ipsum dolor sit amet, consectetur adipiscing elit. Nulla lobortis consequat mauris, eget eleifend nunc viverra viverra. Ut ac risus odio. Aliquam pretium purus sed nulla feugiat blandit. Cras vel libero ut lacus eleifend tempor. Phasellus eleifend, magna non tincidunt accumsan, justo arcu cursus ipsum, non porttitor sapien quam vel magna. Maecenas elit nisl, cursus ipsum, non porttitor justo arcu cursus</p>
<p class="para abs" style="left:89px;top:632px;width:315px">Lorem ipsum dolor sit amet, consectetur adipiscing elit. Nulla lobortis consequat mauris, eget eleifend nunc viverra viverra. Ut ac risus odio. Aliquam pretium purus sed nulla feugiat blandit. Cras vel libero ut lacus eleifend tempor. Phasellus eleifend, magna non tincidunt accumsan, justo arcu cursus ipsum, non porttitor sapien quam vel magna. Maecenas elit nisl, molestie nec dapibus nec, aliquet a erat. Donec scelerisque lacus a libero suscipit auctor volutpat enim euismod. Mauris porta, lacus ut ullamcorper sodales, mauris tortor feugiat purus,</p>
<div class="photo abs" role="img" aria-label="Photo of five business people standing in an office"></div>
<div class="divider abs"></div>

<section class="news abs">
  <div class="news-head"><span>Latest News</span><b><em>1</em>2345</b></div>
  <article class="item">
    <svg class="cal-ico" width="30" height="30" viewBox="0 0 30 30"><rect x="1" y="3" width="28" height="26" fill="#fff" stroke="#888"/><rect x="1" y="3" width="28" height="7" fill="#9c6e08"/><path d="M5 14h20M5 19h20M5 24h20M10 12v15M15 12v15M20 12v15" stroke="#bbb"/></svg>
    <h3>Lorem ipsum dolor sit amet, consectetur adipiscing elit</h3>
    <div class="date">Monday, Friday 15, 2013</div>
    <p>Nulla lobortis consequat mauris, eget eleifend nunc viverra viverra. Ut ac risus odio. Aliquam pretium purus sed nulla feugiat blandit. Cras vel libero ut lacus eleifend tempor. Phasellus eleifend, magna non tincidunt accumsan, justo arcu cursus ipsum, non porttitor sapien quam vel magna. Maecenas elit nisl, molestie nec dapibus nec, Maecenas elit nisl, molestie nec dapibus nec,</p>
  </article>
  <article class="item">
    <svg class="cal-ico" width="30" height="30" viewBox="0 0 30 30"><rect x="1" y="3" width="28" height="26" fill="#fff" stroke="#888"/><rect x="1" y="3" width="28" height="7" fill="#9c6e08"/><path d="M5 14h20M5 19h20M5 24h20M10 12v15M15 12v15M20 12v15" stroke="#bbb"/></svg>
    <h3>Lorem ipsum dolor sit amet, consectetur adipiscing elit</h3>
    <div class="date">Monday, Friday 15, 2013</div>
    <p>Nulla lobortis consequat mauris, eget eleifend nunc viverra viverra. Ut ac risus odio. Aliquam pretium purus sed nulla feugiat blandit. Cras vel libero ut lacus eleifend tempor. Phasellus eleifend, magna non tincidunt accumsan, justo arcu cursus ipsum, non porttitor sapien quam vel magna. Maecenas</p>
  </article>
</section>

<aside class="box abs" style="top:524px;height:134px">
  <h4>User Login</h4>
  <div class="field"><span>Username:</span><i></i></div>
  <div class="field"><span>Password:</span><i></i></div>
  <div class="submit">Submit</div>
</aside>
<aside class="box abs" style="top:672px;height:160px">
  <h4>Testimonials</h4>
  <div class="quote">Lorem ipsum dolor sit amet<em>consectetur adipiscing</em>
    <p>Nulla lobortis consequat mauris, eget eleifend nunc viverra viverra. Ut ac risus odio. Aliquam pretium purus sed nulla feugiat blandit. Cras vel libero ut lacus</p>
  </div>
</aside>
<aside class="box abs" style="top:851px;height:186px">
  <h4>Calender of Events</h4>
  <div class="calendar">
    <div class="cal-head"><small>◀</small><span>July 2013</span><small>▶</small></div>
    <table class="cal">
      <tr><th>MON</th><th>TUE</th><th>WED</th><th>THU</th><th>FRI</th><th>SAT</th><th>SUN</th></tr>
      <tr><td class="o">31</td><td>1</td><td>2</td><td>3</td><td>4</td><td>5</td><td>6</td></tr>
      <tr><td>7</td><td>8</td><td>9</td><td>10</td><td>11</td><td>12</td><td>13</td></tr>
      <tr><td>14</td><td>15</td><td>16</td><td>17</td><td>18</td><td>19</td><td>20</td></tr>
      <tr><td>21</td><td class="h">22</td><td class="h">23</td><td class="h">24</td><td class="h">25</td><td class="h">26</td><td class="h">27</td></tr>
      <tr><td class="h">28</td><td class="h">29</td><td class="h">30</td><td class="o">1</td><td class="o">2</td><td class="o">3</td><td class="o">4</td></tr>
    </table>
  </div>
</aside>

<div class="partners abs"><span>Pavon</span><span>Lumen</span><span>Strata</span><i></i><span class="small">Norvik Classic ERP</span></div>
<div class="footer-links abs">Home | Terms &amp; Conditions | Privacy Policy | Sitemap</div>
<div class="social abs"><i aria-label="Social link"></i><i aria-label="Social link"></i><i aria-label="Social link"></i></div>
<div class="copy abs">© 2013 Ravdu Information Systems PTE LTD. All rights reserved.</div>
</body>
</html>
```